Boutique Real Estate Brokerage looking for business card, letterhead and envelope design

We are looking for a cohesive design for our business cards, letterhead and envelopes and that mirrors our high-end homes and clientele. Cedar & Vane is being launched and designed for the marketplace of tomorrow. We grew from the #1 team in our community into a full-service firm that is going to revolutionize the traditional real estate model.

We understand that it’s more important than ever to help our clients and partners adapt to behavioral and market changes being driven by generational shifts and technological advances in society, and by combining traditional brokerage services with innovative production and marketing capabilities, we know how to do that better than anyone else.

Requirements
Must have
• business card, letterhead and envelope design - attached logo.

```html
<!DOCTYPE html>
<html lang="en">
<head>
<meta charset="utf-8">
<title>Cedar &amp; Vane – Business Card</title>
<link href="https://fonts.googleapis.com/css2?family=Montserrat:wght@600;700&family=Roboto:wght@400&display=swap" rel="stylesheet">
<style>
  :root {
    --bg: #d9d9d6;
    --card-white: #fbfaf7;
    --navy: #1b0c62;
    --navy-deep: #150a52;
    --gold: #c98a45;
    --text-grey: #5a5a5a;
    --watermark: #ecebf0;
    --watermark-warm: #f3ede4;
  }
  * { box-sizing: border-box; margin: 0; padding: 0; }
  html, body { width: 1200px; height: 801px; overflow: hidden; }
  body {
    background: var(--bg);
    position: relative;
    font-family: "Roboto", Arial, sans-serif;
  }
  .card {
    position: absolute;
    top: 246px;
    width: 540px;
    height: 309px;
    box-shadow: 0 6px 18px rgba(0,0,0,0.18);
    overflow: hidden;
  }
  .card-front { left: 40px; background: var(--card-white); }
  .card-back  { left: 620px; background: var(--navy); }

  .front-watermark {
    position: absolute;
    right: 0; top: 0;
    width: 280px; height: 309px;
    background: linear-gradient(160deg, var(--watermark) 0%, var(--watermark-warm) 60%, var(--card-white) 100%);
  }

  .brand {
    position: absolute;
    left: 34px; top: 36px;
    display: flex; align-items: center; gap: 12px;
  }
  .brand-square {
    width: 34px; height: 34px;
    background: var(--navy);
  }
  .brand-name {
    font-family: "Montserrat", Arial, sans-serif;
    font-weight: 700;
    font-size: 24px;
    color: var(--navy);
    letter-spacing: 0.5px;
  }
  .brand-rule {
    position: absolute;
    left: 80px; top: 82px;
    width: 190px; height: 1px;
    background: var(--navy);
  }

  .person { position: absolute; left: 34px; top: 112px; }
  .person-name {
    font-family: "Montserrat", Arial, sans-serif;
    font-weight: 700;
    font-size: 17px;
    color: var(--navy);
    text-transform: uppercase;
  }
  .person-title {
    font-family: "Montserrat", Arial, sans-serif;
    font-weight: 600;
    font-size: 14px;
    color: var(--gold);
    margin-top: 2px;
  }

  .address {
    position: absolute; left: 34px; top: 170px;
    font-size: 13px; line-height: 18px;
    color: var(--text-grey);
  }
  .contact-list {
    position: absolute; left: 34px; top: 214px;
    list-style: none;
    font-size: 13px; line-height: 20px;
    color: var(--text-grey);
  }
  .contact-list li { display: flex; align-items: center; gap: 8px; }
  .contact-icon { width: 12px; height: 12px; flex: none; }

  .back-pattern {
    position: absolute; inset: 0;
    background: linear-gradient(135deg, #1e0f68 0%, var(--navy-deep) 55%, #221070 100%);
  }
  .back-brand {
    position: absolute;
    right: 40px; bottom: 92px;
    font-family: "Montserrat", Arial, sans-serif;
    font-weight: 700;
    font-size: 20px;
    color: var(--gold);
  }
</style>
</head>
<body>

<section class="card card-front" aria-label="Business card front">
  <div class="front-watermark" role="img" aria-label="Large faint brand monogram decoration"></div>

  <div class="brand">
    <span class="brand-square"></span>
    <span class="brand-name">Cedar &amp; Vane</span>
  </div>
  <div class="brand-rule"></div>

  <div class="person">
    <p class="person-name">Martin Hollowell</p>
    <p class="person-title">Managing Director</p>
  </div>

  <p class="address">48 Willow Crest Lane,<br>Maple Ridge, ON L6R 3K2</p>

  <ul class="contact-list">
    <li>
      <svg class="contact-icon" viewBox="0 0 12 12" aria-hidden="true">
        <path d="M2.5 1 L4.5 1 L5 3.5 L3.8 4.5 Q5 7 7.5 8.2 L8.5 7 L11 7.5 L11 9.5 Q11 11 9.5 11 Q1 10.5 1 2.5 Q1 1 2.5 1 Z" fill="var(--navy)"/>
      </svg>
      <span>905.555.0142</span>
    </li>
    <li>
      <svg class="contact-icon" viewBox="0 0 12 12" aria-hidden="true">
        <rect x="0.5" y="2" width="11" height="8" fill="var(--navy)"/>
        <path d="M0.5 2 L6 6.5 L11.5 2" fill="none" stroke="#fff" stroke-width="1"/>
      </svg>
      <span>info@cedarvane.com</span>
    </li>
    <li>
      <svg class="contact-icon" viewBox="0 0 12 12" aria-hidden="true">
        <circle cx="6" cy="6" r="5.5" fill="var(--navy)"/>
        <ellipse cx="6" cy="6" rx="2.2" ry="5.5" fill="none" stroke="#fff" stroke-width="0.8"/>
        <line x1="0.5" y1="6" x2="11.5" y2="6" stroke="#fff" stroke-width="0.8"/>
      </svg>
      <span>www.cedarvane.com</span>
    </li>
  </ul>
</section>

<section class="card card-back" aria-label="Business card back">
  <div class="back-pattern" role="img" aria-label="Repeating tone-on-tone brand monogram pattern"></div>
  <p class="back-brand">Cedar &amp; Vane</p>
</section>

</body>
</html>
```